Stationary for Beauty and Spa School

Create a business card, letterhead and envelopes (primarily #10 envelope with and without window and catalog envelope) for a beauty and wellness school in Miami, Fl. We offer 8 different programs of study and need an eye catching look. Looking for a combination of modern yet sophisticated. Nothing corporate or business looking. Would like to have a look and feel that is similar (or incorporates aspects) of a new website we will be launching in the next 30 days (screen shot attached.)

The final design should communicate style and elegance in a down to earth and friendly way. We strive to provide our students with quality education, friendly and amicable staff and experienced instructors.
Updates

Hello. FYI, in order to print an aesthetically appealing business card, we would like to print them (the business cards) using silk printing method, with spot UV coating (on some elements, maybe the logo, or depending on the design) and die cuts. Please think of this when preparing your design.

Only 1 day left, please submit your designs for selection. Thanks

Target Market(s)

Adults 18-49 years who are mostly interested in beauty and fashion. Need a youthful & modern look, yet sophisticated and elegant.

Industry/Entity Type

School

Colors
e34197
6b449b
add136
f79021

Requirements
Must have
• Similar look and feel as website (see attached screen shot)
Same look and feel of website (see attached screenshot)
Logo
Address: 5216 SW 3rd Avenue. Miami, Fl 33155
Telephone: 305-514-9382
Fax: 786-420-5163
website/url: www.luminora.edu
incorporate Photo of blonde model (attached)
Nice to have
• Tag line: "Beautify your future." Also, maybe two-sided business card. Would be nice if we could mention our programs (maybe in the back of the card). Below are the program offerings (names cannot be changed but order is irrelevant)... Cosmetology, Barber, Spa Therapy, Massage Therapy, Makeup Artistry, Skin Care, Manicure, Pedicure & Nail Extensions, Full Specialist.

A design with text plus a beautiful photo of a model is appealing. Attached to the files is a sample of a cover for a student handbook we have created. You should use the photo of the blonde model (attached) in your design. The original (quality) version of this stock photograph has been uploaded.

Also would be nice to request clients to follow us on facebook and instagram by including the icons.
Should not have
• A corporate or business look. We are a vocational school teaching beauty and spa programs and we like our advertising to have a look that resembles the industry. We do not want a very serious look or snobby feel.

```html
<!DOCTYPE html>
<html lang="en">
<head>
<meta charset="utf-8">
<title>Luminora School of Beauty – Business Card</title>
<link rel="stylesheet" href="https://fonts.googleapis.com/css2?family=Open+Sans:ital,wdth,wght@0,100,300;0,100,400;0,100,600;0,100,700;1,75,300&display=swap">
<style>
  :root {
    --paper: #fffbf3;
    --card-black: #000000;
    --purple: #6b449b;
    --pink: #e34197;
    --orange: #f79021;
    --green: #9dc63a;
    --white: #ffffff;
    --muted: #d8d8d8;
    --watermark: #2a2a2a;
    --watermark-sub: #4a4a4a;
    --photo-light: #f1e6d8;
    --photo-mid: #e0c6ae;
  }
  html, body {
    margin: 0;
    width: 1200px;
    height: 1000px;
    overflow: hidden;
    background: var(--paper);
  }
  .canvas {
    position: relative;
    width: 1200px;
    height: 1000px;
  }
  .card {
    position: absolute;
    top: 63px;
    width: 543px;
    height: 307px;
    display: block;
  }
  .card--front { left: 41px; }
  .card--back { left: 617px; }
  .bg { fill: var(--card-black); }
  .sans { font-family: "Open Sans", Arial, sans-serif; }
  .brand-name { font-size: 36px; font-weight: 600; fill: var(--white); }
  .brand-sub { font-size: 9.5px; font-weight: 600; fill: var(--white); letter-spacing: 0.3px; }
  .holder-name { font-size: 21px; font-weight: 600; fill: var(--white); }
  .holder-role { font-size: 16px; font-weight: 300; fill: var(--muted); }
  .program { font-size: 20.5px; font-weight: 400; fill: var(--white); }
  .bullet { fill: var(--white); }
  .watermark-name { font-size: 58px; font-weight: 600; fill: var(--watermark); }
  .watermark-sub { font-size: 18px; font-weight: 700; fill: var(--watermark-sub); }
  .site { font-size: 26px; font-weight: 400; fill: var(--white); }
  .contact { font-size: 15.5px; font-weight: 400; fill: var(--white); }
  .tagline {
    font-family: "Open Sans", "Arial Narrow", sans-serif;
    font-style: italic;
    font-stretch: 75%;
    font-weight: 300;
    font-size: 27px;
    fill: var(--white);
  }
</style>
</head>
<body>
<main class="canvas">

  <!-- Front of card -->
  <svg class="card card--front" viewBox="0 0 543 307" aria-label="Business card front">
    <defs>
      <clipPath id="front-edge"><rect width="543" height="307"/></clipPath>
      <radialGradient id="model-tones" cx="0.35" cy="0.45" r="0.7">
        <stop offset="0" stop-color="var(--photo-light)"/>
        <stop offset="0.6" stop-color="var(--photo-mid)"/>
        <stop offset="1" stop-color="var(--photo-light)"/>
      </radialGradient>
      <linearGradient id="front-wave-tones" x1="0" y1="0" x2="0.15" y2="1">
        <stop offset="0" stop-color="var(--purple)"/>
        <stop offset="0.22" stop-color="var(--pink)"/>
        <stop offset="0.38" stop-color="var(--orange)"/>
        <stop offset="0.55" stop-color="var(--green)"/>
        <stop offset="1" stop-color="var(--green)"/>
      </linearGradient>
    </defs>
    <g clip-path="url(#front-edge)">
      <rect class="bg" width="543" height="307"/>
      <circle cx="115" cy="75" r="210" fill="url(#model-tones)" role="img" aria-label="Portrait photo of a blonde model"/>
      <path fill="url(#front-wave-tones)" role="img" aria-label="Decorative colour wave in the school palette"
            d="M0 307 L0 282 C190 300 340 175 543 115 L543 307 Z"/>
    </g>
    <text class="sans brand-name" x="515" y="78" text-anchor="end">Luminora</text>
    <text class="sans brand-sub" x="493" y="92" text-anchor="end">SCHOOL OF BEAUTY</text>
    <text class="sans holder-name" x="515" y="246" text-anchor="end">Name Surname</text>
    <text class="sans holder-role" x="515" y="270" text-anchor="end">position</text>
  </svg>

  <!-- Back of card -->
  <svg class="card card--back" viewBox="0 0 543 307" aria-label="Business card back">
    <defs>
      <clipPath id="back-edge"><rect width="543" height="307"/></clipPath>
      <linearGradient id="back-wave-tones" x1="0" y1="0" x2="0.1" y2="1">
        <stop offset="0" stop-color="var(--purple)"/>
        <stop offset="0.2" stop-color="var(--pink)"/>
        <stop offset="0.36" stop-color="var(--orange)"/>
        <stop offset="0.52" stop-color="var(--green)"/>
        <stop offset="1" stop-color="var(--green)"/>
      </linearGradient>
    </defs>
    <g clip-path="url(#back-edge)">
      <rect class="bg" width="543" height="307"/>
      <text class="sans watermark-name" x="175" y="122">Luminora</text>
      <text class="sans watermark-sub" x="166" y="155">SCHOOL OF BEAUTY</text>
      <path fill="url(#back-wave-tones)" role="img" aria-label="Decorative colour wave in the school palette"
            d="M192 307 C300 294 420 175 543 150 L543 307 Z"/>
    </g>

    <g class="programs">
      <circle class="bullet" cx="39" cy="49" r="2.2"/><text class="sans program" x="53" y="56">Cosmetology</text>
      <circle class="bullet" cx="39" cy="76" r="2.2"/><text class="sans program" x="53" y="83">Barber</text>
      <circle class="bullet" cx="39" cy="103" r="2.2"/><text class="sans program" x="53" y="110">Spa Therapy</text>
      <circle class="bullet" cx="39" cy="130" r="2.2"/><text class="sans program" x="53" y="137">Skin Care</text>
      <circle class="bullet" cx="39" cy="157" r="2.2"/><text class="sans program" x="53" y="164">Manicure</text>
      <circle class="bullet" cx="39" cy="184" r="2.2"/><text class="sans program" x="53" y="191">Pedicure &amp; Nail Extensions</text>
      <circle class="bullet" cx="39" cy="211" r="2.2"/><text class="sans program" x="53" y="218">Massage Therapy</text>
      <circle class="bullet" cx="39" cy="238" r="2.2"/><text class="sans program" x="53" y="245">Makeup Artistry</text>
      <circle class="bullet" cx="39" cy="265" r="2.2"/><text class="sans program" x="53" y="272">Full Specialist</text>
    </g>

    <text class="sans site" x="512" y="56" text-anchor="end">www.luminora.edu</text>
    <text class="sans contact" x="512" y="94" text-anchor="end">5216 SW 3rd Avenue. Miami, Fl 33155</text>
    <text class="sans contact" x="512" y="114" text-anchor="end">Telephone: 305-514-9382</text>
    <text class="sans contact" x="512" y="134" text-anchor="end">Fax: 786-420-5163</text>

    <text class="tagline" x="517" y="277" text-anchor="end">Beautify your future</text>
  </svg>

</main>
</body>
</html>
```